Book cover for a book on tactics, habits and directives learned from world class performers

The Steady Routines book is the first in a series of four books filled with proven tactics, habits and directives (i.e., what to do) that young, ambitious working professionals should be doing to make their life better. The first book is on foundational or keystone habits - that is, the habits that will help everyone upgrade their life and enable other great habits in their life (things such as waking up early in the morning or exercising)

The goal of the book is to stand out on the Orbello platform as a small thumbnail, as well as a 5 x 8 book.

The imagery should make the viewer feel that the book (and the author) are the authority in habits and developing habits.

The reader should feel that they must have this book if they know they should be developing successful habits but do not want to comb through hundreds of books just to find the one tactic or habit that they should be doing. It's important that the book "pops off the shelf" and catches the eye quickly.

The most important part of the design is that it sells, not that it looks well-designed. I am open to any image or illustration you choose though please consider the nice have I have listed below. Here are a few words that come to mind when thinking of my book: growth, self development, leadership, success, freedom, passion, motivation, young professional, accomplished, experience.

I like a bold color palette. I like bold titles that you know right away what the title is and what it is about, not too busy and with simple color schemes. 2 - 3 colors.

Books with covers I like:
- Night Venture by Dorian Flemwick
- Our Finest Season Yet by Gerald Pomfret
- The Fortune Outlook by Warren Ketterby

Target Market(s)

- Young 20 - 40 year old ambitious working professionals interested in self development and listen to podcasts of Lou Brandvik, Oscar Menderlin
- Just starting out management consultants

Colors

Designer to choose colors to be used in the design.

Requirements
Must have
• 'Steady Routines' title - first and foremost
• Author name - Lo Chen - probably on the bottom or somewhere
• Bold colour / colours or a graphic that is eye catching (and makes it different from other habits books on Orbello)
Nice to have
• Would like to have some sort of visual, colour or theme that can run through the four books - would be great to have a cover design that can be simply changed to depict the second, third or fourth book in the series - maybe the graphic or visual can be changed with some colours, etc. but with the overall feel looking similar so that people can see that it's part of the same book series

```html
<!DOCTYPE html>
<html lang="en">
<head>
<meta charset="utf-8">
<title>Steady Routines — Lo Chen</title>
<link rel="stylesheet" href="https://fonts.googleapis.com/css2?family=Anton&family=Cinzel:wght@400;500&display=swap">
<style>
  :root {
    --paper: #ffffff;
    --ink: #141414;
    --cover-red: #c0212b;
    --cover-red-deep: #a11a23;
    --cover-red-shadow: #8e161e;
    --author-white: #ffffff;
  }
  * { margin: 0; padding: 0; box-sizing: border-box; }
  html, body {
    width: 737px;
    height: 1200px;
    overflow: hidden;
    background: var(--paper);
  }
  .book-cover {
    position: relative;
    width: 737px;
    height: 1200px;
    background: var(--paper);
    overflow: hidden;
  }
  .title-block {
    position: absolute;
    left: 0;
    top: 0;
    width: 737px;
    height: 561px;
    background: var(--paper);
  }
  .title-block svg { display: block; }
  .title-kicker {
    font-family: "Anton", "Impact", sans-serif;
    fill: var(--ink);
  }
  .title-main {
    font-family: "Anton", "Impact", sans-serif;
    fill: var(--cover-red);
  }
  .cover-visual {
    position: absolute;
    left: 0;
    top: 561px;
    width: 737px;
    height: 639px;
    background:
      radial-gradient(ellipse 60% 45% at 38% 28%, var(--cover-red) 0%, var(--cover-red-deep) 70%, var(--cover-red-shadow) 100%);
  }
  .author-name {
    position: absolute;
    left: 0;
    right: 0;
    top: 1086px;
    text-align: center;
    font-family: "Cinzel", "Times New Roman", serif;
    font-weight: 400;
    font-size: 60px;
    letter-spacing: 0.14em;
    color: var(--author-white);
    line-height: 1;
  }
</style>
</head>
<body>
  <main class="book-cover">
    <header class="title-block">
      <svg width="737" height="561" viewBox="0 0 737 561" aria-labelledby="cover-title">
        <title id="cover-title">Steady Routines</title>
        <text class="title-kicker" x="78" y="204" font-size="80"
              textLength="588" lengthAdjust="spacing">STEADY</text>
        <text class="title-main" x="76" y="408" font-size="232"
              textLength="592" lengthAdjust="spacingAndGlyphs">ROUTINES</text>
      </svg>
    </header>
    <section class="cover-visual" role="img" aria-label="Black twin-bell alarm clock on a red surface, hands just before twelve"></section>
    <p class="author-name">Lo Chen</p>
  </main>
</body>
</html>
```